Label designs for three different cider varieties

The Larkmoor Perry Works is a family run business. We have been making cider within the family as a hobby for over 100 years and we have recently decided to start to try to sell the cider. Therefore this project is to create a logo and three product labels for three different varieties of cider. So we should end up with four files; one for the logo and one for each of the labels. The files need to be in an editable format for us so that we can add edit the batch numbers e.g. PNG file.
For the logo we would like to use the Pellow Family Shield since Pellow is our family name. We would like it adapted into a cider themed crest, for example with apples and trees. We are open to ideas about the logo but this is just our initial idea. Example of the original Pellow Family Shield can be seen in the link below:
http://www.vinshadeheraldry.net/arms/Pellow-England.jpg
The labels should be no bigger than 93mm in height and 213mm in length. Each label should be similar in style so it is clear the three different varieties of cider are from the same company. Each label must have the following information since this is a legal requirement:
- The logo you have created
- The Larkmoor Perry Works Ltd.
- 52 Mirefield Row, Taunton, Somerset, TA4 9QX
- Alcohol: 6% vol
- 500ml
- Allergens: Contains Sulphites for freshness
- There needs to be space on the label for batch numbers. This is four numbers e.g. 1701.
- Family craft cider makers using only premium apples from our own traditional Somerset orchard.
The names of the three cider varieties are:
- Larkmoor Heritage
- Larkmoor Amber
- Larkmoor Kingsbury
Our initial idea is that each variety would have its own colour associated with it; i.e. black themed label for Larkmoor Heritage, gold themed label for Larkmoor Amber and a red themed label for Larkmoor Kingsbury. The crest logo you have created would then be in the themed colour for that cider variety i.e. black, gold or red.
We would like the labels to reflect the following themes for our brand:
- High end premium brand
- Clean and simple design
- Modern
Overall we are very open to ideas and we do not want to constrain your creativity. All of the above is just our initial ideas but we would love to see what ideas you have. The only things that cannot change are what must be on the label since this is a legal requirement we have to meet.

```html
<!DOCTYPE html>
<html lang="en">
<head>
<meta charset="utf-8">
<title>Larkmoor Perry Works – Labels and Logo</title>
<link rel="stylesheet" href="https://fonts.googleapis.com/css2?family=Montserrat:wght@600;700;800&family=Oswald:wght@500;600;700&display=swap">
<style>
:root{
  --ink:#111111;
  --paper:#ffffff;
  --heritage:#2e3530;
  --amber:#a0940e;
  --kingsbury:#5e0a14;
  --art-light:#ededed;
  --art-mid:#d9d9d9;
  --frame:#9a9a9a;
}
*{box-sizing:border-box;margin:0;padding:0}
html,body{width:1200px;height:1000px;overflow:hidden;background:var(--paper)}
.canvas{position:relative;width:1200px;height:1000px;background:var(--paper);font-family:"Montserrat",Arial,sans-serif;color:var(--ink)}

/* ---- product label ---- */
.label{position:absolute;left:0;width:786px;height:327px;border:1px solid var(--frame);background:var(--paper);overflow:hidden}
.label--heritage{top:0;--band:var(--heritage)}
.label--amber{top:335px;--band:var(--amber)}
.label--kingsbury{top:673px;--band:var(--kingsbury)}

.art-area{position:absolute;background:linear-gradient(180deg,var(--art-light),var(--art-mid))}
.art-area--tree-left{left:12px;top:56px;width:244px;height:184px}
.art-area--tree-right{left:540px;top:56px;width:240px;height:184px}
.art-area--crest{left:340px;top:2px;width:80px;height:96px}

.maker-line{position:absolute;left:0;width:756px;text-align:center;font-weight:700;line-height:1}
.maker-line--orchard{top:97px;font-size:8px}
.maker-line--company{top:107px;font-size:9.5px}

.variety-name{position:absolute;left:178px;width:400px;top:116px;text-align:center;font-weight:700;font-size:27px;line-height:1;white-space:nowrap}
.variety-rule{position:absolute;left:248px;width:280px;top:150px;height:5px;background:var(--ink)}
.product-word{position:absolute;left:240px;width:296px;top:146px;text-align:center;font-family:"Oswald","Arial Narrow",sans-serif;font-weight:700;font-size:94px;line-height:1.02;letter-spacing:1px}

.band{position:absolute;left:0;right:0;bottom:0;height:87px;background:var(--band);font-family:"Oswald","Arial Narrow",sans-serif;color:var(--ink)}
.info-panel{position:absolute;left:253px;top:5px;width:270px;height:78px;border:1px solid rgba(255,255,255,.45)}
.info-panel__story{position:absolute;left:4px;top:9px;width:110px;font-size:7.4px;line-height:1.42;font-weight:500}
.info-panel__story span{display:block;text-align:justify;text-align-last:justify}
.info-panel__story span:last-child{text-align-last:center}
.info-panel__rule{position:absolute;left:3px;top:67px;width:108px;height:4px;background:var(--ink)}
.info-panel__headline{position:absolute;left:116px;top:5px;width:150px;text-align:center;font-size:16px;font-weight:700;line-height:1.2}
.info-panel__headline span{display:block}
.info-panel__sub{font-size:14px;letter-spacing:1px}
.apple-row{position:absolute;left:118px;top:52px;width:90px;height:16px}
.abv{position:absolute;left:226px;top:51px;font-size:11px;font-weight:700}
.volume{position:absolute;left:14px;top:60px;font-size:13px;font-weight:700}
.allergens{position:absolute;left:60px;top:67px;font-size:6.8px;font-weight:500}
.producer{position:absolute;left:553px;top:46px;font-size:7.4px;font-weight:600;line-height:2.3}

/* ---- logo sheet ---- */
.logo{position:absolute;left:800px;width:400px;text-align:center}
.logo--colour{top:185px}
.logo--mono{top:625px}
.logo-art{margin:0 auto;height:275px;width:325px;background:linear-gradient(180deg,var(--art-light),var(--art-mid))}
.logo__orchard{font-weight:700;font-size:20px;line-height:1;margin-top:10px}
.logo__company{font-weight:700;font-size:25px;line-height:1;margin-top:7px;white-space:nowrap}
.logo--colour .logo__orchard{color:var(--amber)}
.logo--colour .logo__company{color:var(--heritage)}
.logo--mono .logo__orchard{color:var(--ink);margin-top:14px}
.logo--mono .logo__company{color:var(--ink)}
</style>
</head>
<body>
<div class="canvas">

  <!-- Heritage label -->
  <section class="label label--heritage">
    <div class="art-area art-area--tree-left" role="img" aria-label="Engraved apple tree illustration"></div>
    <div class="art-area art-area--tree-right" role="img" aria-label="Engraved apple tree illustration"></div>
    <div class="art-area art-area--crest" role="img" aria-label="Family shield emblem set in a small orchard tree"></div>
    <p class="maker-line maker-line--orchard">ORCHARD &amp; CIDERY</p>
    <p class="maker-line maker-line--company">LARKMOOR PERRY WORKS</p>
    <h2 class="variety-name">LARKMOOR HERITAGE</h2>
    <div class="variety-rule"></div>
    <p class="product-word">CYDER</p>
    <div class="band">
      <p class="volume">500ml</p>
      <p class="allergens">ALLERGENS: CONTAINS SULPHITES FOR FRESHNESS</p>
      <div class="info-panel">
        <p class="info-panel__story"><span>FAMILY CRAFT CIDER MAKERS</span><span>USING ONLY PREMIUM APPLES</span><span>FROM OUR OWN TRADITIONAL</span><span>SOMERSET ORCHARD.</span></p>
        <div class="info-panel__rule"></div>
        <p class="info-panel__headline"><span>SMALL BATCH CIDER</span><span class="info-panel__sub">FROM SOMERSET</span></p>
        <svg class="apple-row" viewBox="0 0 90 16" aria-hidden="true" fill="none" stroke="#111" stroke-width="1.3"><g><circle cx="8" cy="10" r="5"/><path d="M8 5V2M8 4l3-2"/></g><g transform="translate(18 0)"><circle cx="8" cy="10" r="5"/><path d="M8 5V2M8 4l3-2"/></g><g transform="translate(36 0)"><circle cx="8" cy="10" r="5"/><path d="M8 5V2M8 4l3-2"/></g><g transform="translate(54 0)"><circle cx="8" cy="10" r="5"/><path d="M8 5V2M8 4l3-2"/></g><g transform="translate(72 0)"><circle cx="8" cy="10" r="5"/><path d="M8 5V2M8 4l3-2"/></g></svg>
        <p class="abv">6% VOL</p>
      </div>
      <p class="producer">THE LARKMOOR PERRY WORKS LTD.<br>52 MIREFIELD ROW, TAUNTON, SOMERSET, TA4 9QX</p>
    </div>
  </section>

  <!-- Amber label -->
  <section class="label label--amber">
    <div class="art-area art-area--tree-left" role="img" aria-label="Engraved apple tree illustration"></div>
    <div class="art-area art-area--tree-right" role="img" aria-label="Engraved apple tree illustration"></div>
    <div class="art-area art-area--crest" role="img" aria-label="Family shield emblem set in a small orchard tree"></div>
    <p class="maker-line maker-line--orchard">ORCHARD &amp; CIDERY</p>
    <p class="maker-line maker-line--company">LARKMOOR PERRY WORKS</p>
    <h2 class="variety-name">LARKMOOR AMBER</h2>
    <div class="variety-rule"></div>
    <p class="product-word">CYDER</p>
    <div class="band">
      <p class="volume">500ml</p>
      <p class="allergens">ALLERGENS: CONTAINS SULPHITES FOR FRESHNESS</p>
      <div class="info-panel">
        <p class="info-panel__story"><span>FAMILY CRAFT CIDER MAKERS</span><span>USING ONLY PREMIUM APPLES</span><span>FROM OUR OWN TRADITIONAL</span><span>SOMERSET ORCHARD.</span></p>
        <div class="info-panel__rule"></div>
        <p class="info-panel__headline"><span>SMALL BATCH CIDER</span><span class="info-panel__sub">FROM SOMERSET</span></p>
        <svg class="apple-row" viewBox="0 0 90 16" aria-hidden="true" fill="none" stroke="#111" stroke-width="1.3"><g><circle cx="8" cy="10" r="5"/><path d="M8 5V2M8 4l3-2"/></g><g transform="translate(18 0)"><circle cx="8" cy="10" r="5"/><path d="M8 5V2M8 4l3-2"/></g><g transform="translate(36 0)"><circle cx="8" cy="10" r="5"/><path d="M8 5V2M8 4l3-2"/></g><g transform="translate(54 0)"><circle cx="8" cy="10" r="5"/><path d="M8 5V2M8 4l3-2"/></g><g transform="translate(72 0)"><circle cx="8" cy="10" r="5"/><path d="M8 5V2M8 4l3-2"/></g></svg>
        <p class="abv">6% VOL</p>
      </div>
      <p class="producer">THE LARKMOOR PERRY WORKS LTD.<br>52 MIREFIELD ROW, TAUNTON, SOMERSET, TA4 9QX</p>
    </div>
  </section>

  <!-- Kingsbury label -->
  <section class="label label--kingsbury">
    <div class="art-area art-area--tree-left" role="img" aria-label="Engraved apple tree illustration"></div>
    <div class="art-area art-area--tree-right" role="img" aria-label="Engraved apple tree illustration"></div>
    <div class="art-area art-area--crest" role="img" aria-label="Family shield emblem set in a small orchard tree"></div>
    <p class="maker-line maker-line--orchard">ORCHARD &amp; CIDERY</p>
    <p class="maker-line maker-line--company">LARKMOOR PERRY WORKS</p>
    <h2 class="variety-name">LARKMOOR KINGSBURY</h2>
    <div class="variety-rule"></div>
    <p class="product-word">CYDER</p>
    <div class="band">
      <p class="volume">500ml</p>
      <p class="allergens">ALLERGENS: CONTAINS SULPHITES FOR FRESHNESS</p>
      <div class="info-panel">
        <p class="info-panel__story"><span>FAMILY CRAFT CIDER MAKERS</span><span>USING ONLY PREMIUM APPLES</span><span>FROM OUR OWN TRADITIONAL</span><span>SOMERSET ORCHARD.</span></p>
        <div class="info-panel__rule"></div>
        <p class="info-panel__headline"><span>SMALL BATCH CIDER</span><span class="info-panel__sub">FROM SOMERSET</span></p>
        <svg class="apple-row" viewBox="0 0 90 16" aria-hidden="true" fill="none" stroke="#111" stroke-width="1.3"><g><circle cx="8" cy="10" r="5"/><path d="M8 5V2M8 4l3-2"/></g><g transform="translate(18 0)"><circle cx="8" cy="10" r="5"/><path d="M8 5V2M8 4l3-2"/></g><g transform="translate(36 0)"><circle cx="8" cy="10" r="5"/><path d="M8 5V2M8 4l3-2"/></g><g transform="translate(54 0)"><circle cx="8" cy="10" r="5"/><path d="M8 5V2M8 4l3-2"/></g><g transform="translate(72 0)"><circle cx="8" cy="10" r="5"/><path d="M8 5V2M8 4l3-2"/></g></svg>
        <p class="abv">6% VOL</p>
      </div>
      <p class="producer">THE LARKMOOR PERRY WORKS LTD.<br>52 MIREFIELD ROW, TAUNTON, SOMERSET, TA4 9QX</p>
    </div>
  </section>

  <!-- Logo, colour version -->
  <section class="logo logo--colour">
    <div class="logo-art" role="img" aria-label="Colour emblem: family shield set in an engraved apple tree with red fruit"></div>
    <p class="logo__orchard">ORCHARD &amp; CIDERY</p>
    <p class="logo__company">LARKMOOR PERRY WORKS</p>
  </section>

  <!-- Logo, mono version -->
  <section class="logo logo--mono">
    <div class="logo-art" role="img" aria-label="Black and white emblem: family shield set in an engraved apple tree"></div>
    <p class="logo__orchard">ORCHARD &amp; CIDERY</p>
    <p class="logo__company">LARKMOOR PERRY WORKS</p>
  </section>

</div>
</body>
</html>
```